Buch-/E-Book-Cover im Bereich der Persönlichkeitsentwicklung
Vielen lieben Dank für die super Arbeit von Dir. Das Design ist klasse und die vielen Vorschläge waren auch super. Die komplette Zusammenarbeit verlief sehr professionell und Änderungswünsche wurden sehr schnell umgesetzt. Ich kann Dich voll und ganz weiterempfehlen.
Zielgruppe
Wir arbeiten in der Persönlichkeitsentwicklung für Jugendliche. Dabei spezialisieren wir uns auf den Altersbereich 12 - 17 Jahre. Unser Ziel ist es jungen Menschen zu zeigen, wie Sie zu sich selbst finden und ein glückliches sowie erfolgreiches Leben führen können.
Aufgabenstellung
- Das Design sollte für die Eltern von Teenagern und auch für die Teenager selbst ausgelegt werden. Das Buch ist für die Jugendlichen (Mädchen und Jungen im Alter zwischen 12 Jahren und 17 Jahren) gedacht, wird allerdings meist von deren Mütter gekauft.
- Der Name des Autors lautet: Jochen Brabeck
- Der Titel lautet: Junge Leute finden Mut und Richtung
- Der Untertitel lautet: Was Heranwachsende über eigene Stärken lernen
- Im Anhang befinden sich Designs, die ich gut finde (nur falls jemand weitere Ideen haben möchte)
- Format: 15,24 cm x 22,86 cm (6' x 9') [genaue Maße fürs Taschenbuch und Hardcover sind im Anhang (.zip Dateien)]
1. E-Book:
- Coverdateien sollten idealerweise 2 560 Pixel hoch und 1 600 Pixel breit sein. Zur Gewährleistung der bestmöglichen Qualität (insbesondere auf HD-Geräten) sollte das Bild mindestens 2 500 Pixel hoch sein.
- Format: TIFF (.tif/.tiff) oder JPEG (.jpeg/.jpg)
- DPI: 72 dpi
- Größe: Ihr Coverbild muss kleiner als 50 MB sein.
Hinweis: Vermeiden Sie es, Ihre Dateien zu komprimieren. Dies kann die Qualität Ihres Covers auf Lesegeräten beeinträchtigen. Das beste Ergebnis erzielen Sie mit Bildern, die eine Mindestauflösung von 300 ppi (Pixels per Inch) haben.
- Rahmen: Coverbilder mit weißem oder sehr hellem Hintergrund heben sich kaum vom weißen Hintergrund ab. Fügen Sie einen dünnen Rahmen (3–4 Pixel) in Mittelgrau hinzu, um die Ränder des Covers besser sichtbar zu machen.
2. + 3. Taschenbuch/Hardcover [genaue Maße fürs Taschenbuch und Hardcover sind im Anhang (.zip Dateien)] :
- Dateityp: Das Cover muss als einzelne PDF-Datei vorliegen und die hintere Coverseite, den Buchrücken und die vordere Coverseite als einzelnes Bild enthalten.
- Dateigröße: Coverdateien, die größer als 650 MB sind, können nicht konvertiert werden. Die Datei sollte maximal 40 MB groß sein, da sich bei großen Dateien der Druck verlangsamt.
- Die gen..

```html
<!DOCTYPE html>
<html lang="de">
<head>
<meta charset="utf-8">
<title>Junge Leute finden Mut und Richtung – Umschlag</title>
<link rel="stylesheet" href="https://fonts.googleapis.com/css2?family=Barlow+Condensed:wght@400;500;700&family=Londrina+Solid:wght@400;900&family=Amatic+SC:wght@400;700&family=Dosis:wght@300;400&display=swap">
<style>
  :root {
    --page: #ffffff;
    --ink: #1c1c1c;
    --white: #ffffff;
    --sky-back-top: #80b5df;
    --sky-back-bottom: #d9eef6;
    --sky-front-top: #4f8cca;
    --sky-front-bottom: #a9d5ef;
    --rock: #6f6558;
    --rock-light: #948a7b;
    --divider: #e8f2f8;
  }
  * { margin: 0; padding: 0; box-sizing: border-box; }
  html, body { width: 1200px; height: 880px; overflow: hidden; background: var(--page); }
  .canvas { position: relative; width: 1200px; height: 880px; }

  .jacket { position: absolute; left: 39px; top: 45px; width: 1122px; height: 788px; display: flex; }

  /* Back cover */
  .back {
    position: relative; width: 525px; height: 100%;
    background: linear-gradient(180deg, var(--sky-back-top) 0%, #a9d3ec 45%, var(--sky-back-bottom) 100%);
    font-family: "Barlow Condensed", sans-serif; color: var(--ink);
  }
  .back-copy { position: absolute; left: 43px; top: 48px; width: 370px; }
  .back-headline { font-weight: 700; font-size: 16px; line-height: 1.2; margin-bottom: 8px; }
  .back-copy p { font-size: 13px; line-height: 17.5px; margin-bottom: 17px; }
  .back-list-intro { font-weight: 700; font-size: 13.5px; margin-bottom: 4px; }
  .back-list { list-style: none; font-size: 13px; line-height: 17.6px; }
  .back-list li::before { content: "· "; font-weight: 700; }
  .testimonial {
    position: absolute; left: 181px; top: 548px; width: 310px;
    font-family: "Amatic SC", sans-serif; font-weight: 700; font-size: 24px; line-height: 25px;
  }
  .testimonial cite { display: block; font-style: normal; margin-top: 6px; }

  /* Spine */
  .spine {
    position: relative; width: 73px; height: 100%;
    border-left: 1px solid var(--divider); border-right: 1px solid var(--divider);
    background: linear-gradient(180deg, #6ea7da 0%, #a6d0ea 60%, #c8e5f3 100%);
  }
  .spine-title, .spine-author {
    position: absolute; left: 50%; writing-mode: vertical-rl;
    transform: translateX(-50%) rotate(180deg); white-space: nowrap;
  }
  .spine-title { top: 52px; color: var(--white); font-family: "Londrina Solid", sans-serif; font-size: 30px; }
  .spine-title .light { font-family: "Dosis", sans-serif; font-weight: 300; font-size: 24px; }
  .spine-author { top: 600px; font-family: "Barlow Condensed", sans-serif; font-weight: 700; font-size: 22px; letter-spacing: 1px; color: var(--ink); }

  /* Front cover */
  .front {
    position: relative; flex: 1; height: 100%;
    background: linear-gradient(180deg, var(--sky-front-top) 0%, #7eb5e1 45%, var(--sky-front-bottom) 100%);
  }
  .front-author {
    position: absolute; top: 26px; left: 0; right: 0; text-align: center;
    font-family: "Barlow Condensed", sans-serif; font-weight: 700; font-size: 24px; letter-spacing: 1.5px; color: var(--ink);
  }
  .front-title { position: absolute; left: 48px; top: 110px; width: 440px; color: var(--white); font-family: "Londrina Solid", sans-serif; font-weight: 900; }
  .front-title .big { display: block; font-size: 86px; line-height: 80px; }
  .front-title .small { font-family: "Dosis", sans-serif; font-weight: 300; font-size: 40px; }
  .front-title .line-2 { display: block; text-align: right; padding-right: 30px; line-height: 44px; }
  .front-title .line-4 { text-align: right; }
  .front-subtitle {
    position: absolute; left: 40px; top: 418px; width: 200px; text-align: right;
    font-family: "Amatic SC", sans-serif; font-weight: 700; font-size: 27px; line-height: 31px; color: var(--ink);
  }
  .front-photo {
    position: absolute; left: 48px; top: 535px; right: 0; bottom: 0;
    background: linear-gradient(180deg, rgba(169,213,239,0) 0%, rgba(169,213,239,0.2) 30%, var(--rock-light) 58%, var(--rock) 100%);
  }
</style>
</head>
<body>
<div class="canvas">
  <div class="jacket">
    <section class="back">
      <div class="back-copy">
        <h2 class="back-headline">Dein wahres Selbst verändert Dein Leben ins Positive.</h2>
        <p>Glaubst Du, dass Du zu mehr in der Lage bist? Geraten deine Träume wegen Verpflichtungen, Ängsten und dem Alltag in den Hintergrund? Würdest Du gerne ein Mittel haben, das gegen Leistungsdruck und Zeitmangel hilft? Denkst Du, dass Du mit der richtigen Lebensweise ein komplett anderes, viel erfüllteres Leben führen könntest? Dieses Buch zeigt dir den Weg dahin.</p>
        <p>Im Gegensatz zu zahlreichen anderen Ratgebern wird in diesem Buch das Thema Selbstfindung viel tiefgehender und individueller betrachtet. Häufig wird nur sehr oberflächlich nach dem idealen Beruf gesucht, darüber geschrieben, wie wir unseren Alltag verbringen sollten oder wie Du zu dir selbst findest. Deshalb erhältst Du hier einige lebensnahe Praxisbeispiele, die Du sofort anwenden kannst.</p>
        <div class="back-list-intro">In diesem Buch lernst Du unter anderem, wie Du</div>
        <ul class="back-list">
          <li>den passenden Beruf findest.</li>
          <li>dich von Ängsten befreien kannst.</li>
          <li>Klarheit darüber erlangst, was Du in deinem Leben willst.</li>
          <li>innere und äußere Freiheit erlangst.</li>
          <li>mit dem richtigen Mindset, mehr Energie bekommst.</li>
          <li>in die Umsetzung kommst.</li>
          <li>mit Deinen Gefühlen umgehen kannst.</li>
        </ul>
      </div>
      <blockquote class="testimonial">
        „Das KOMPASS-Prinzip hat mich sehr beeindruckt und nachhaltig beeinflusst. Es ist absolut lesenswert und im Vergleich zu anderen Ratgebern spricht es den Leser direkt an und motiviert zum Handeln und Nachdenken.“
        <cite>Lehrerin Fr. Albers</cite>
      </blockquote>
    </section>

    <section class="spine">
      <div class="spine-title">Junge Leute <span class="light">finden</span> Mut <span class="light">und</span> Richtung</div>
      <div class="spine-author">JOCHEN BRABECK</div>
    </section>

    <section class="front">
      <div class="front-author">JOCHEN BRABECK</div>
      <h1 class="front-title">
        <span class="big">Junge Leute</span>
        <span class="small line-2">finden</span>
        <span class="big">Mut <span class="small">und</span></span>
        <span class="big line-4">Richtung</span>
      </h1>
      <p class="front-subtitle">WAS HERANWACHSENDE ÜBER EIGENE STÄRKEN LERNEN</p>
      <div class="front-photo" role="img" aria-label="Foto: vier Jugendliche sitzen vor blauem Himmel auf einer Felsmauer und unterhalten sich"></div>
    </section>
  </div>
</div>
</body>
</html>
```